One page website

I'm looking for a landing page for my company. Just a brief description of our medical device technology with some images

Coding

Coded - Design and coding required

```html
<!DOCTYPE html>
<html lang="en">
<head>
<meta charset="utf-8">
<title>Vertara Surgical – Solving Children's Scoliosis</title>
<link href="https://fonts.googleapis.com/css2?family=Cabin:wght@400;500;600;700&family=Montserrat:ital,wght@0,300;0,400;0,500;0,600;0,700;1,700&display=swap" rel="stylesheet">
<style>
:root{
  --green:#8dc63f;
  --green-dark:#76b02d;
  --blue:#2aa3dc;
  --cyan:#45bde9;
  --blue-deep:#1f8fc9;
  --ink:#444;
  --muted:#666;
  --panel:#f1f2f3;
  --white:#fff;
}
*{margin:0;padding:0;box-sizing:border-box}
html,body{width:1200px;height:4882px;overflow:hidden;background:var(--white)}
body{position:relative;font-family:"Montserrat",sans-serif;color:var(--ink)}
.abs{position:absolute}
.shapes{position:absolute;left:0;top:0;width:1200px;height:4882px}
h1,h2,h3{font-family:"Cabin",sans-serif;font-weight:500}

/* header */
.brand{left:92px;top:62px;font-family:"Cabin",sans-serif;font-weight:600;font-size:30px;color:var(--green);line-height:1}
.brand small{display:block;font-size:16px;text-align:center;margin-top:2px}
.phone-tab{left:864px;top:0;width:236px;height:42px;background:var(--green);border-radius:0 0 14px 14px;color:#fff;font-weight:600;font-size:20px;display:flex;align-items:center;justify-content:center;gap:8px}
.follow{left:954px;top:56px;color:var(--blue);font-weight:600;font-size:17px}
.social{left:922px;top:83px;display:flex;gap:4px}
.social span{width:21px;height:21px;background:var(--blue);border-radius:2px}
.social span:nth-child(5){background:#d2412f}.social span:nth-child(6){background:#c8232c}
.nav{left:0;top:136px;width:1200px;height:35px;background:var(--blue)}
.nav a{position:absolute;top:8px;color:#fff;font-size:16px;text-decoration:none;font-family:"Cabin",sans-serif}
.nav .home{left:92px;top:0;width:105px;height:35px;background:var(--green);padding-top:8px;text-align:center}
.vbt-btn{left:910px;top:128px;width:200px;height:46px;background:var(--green);border:2px solid #fff;color:#fff;font-family:"Cabin",sans-serif;font-weight:600;font-size:19px;letter-spacing:1px;display:flex;align-items:center;justify-content:center}

/* hero */
.hero-title{left:56px;top:278px;color:#fff;font-family:"Cabin",sans-serif;font-weight:700;font-size:80px;line-height:84px;letter-spacing:1px}
.hero-side{right:46px;top:330px;text-align:right;color:#fff}
.hero-side h2{font-size:27px;color:#1f4f73;font-weight:400;letter-spacing:.5px}
.hero-side p{font-size:19px;line-height:25px;margin-top:8px}
.know-more{right:57px;top:470px;width:120px;height:23px;background:var(--green);color:#fff;font-size:12px;font-weight:600;letter-spacing:1px;display:flex;align-items:center;justify-content:center}

/* about */
.about-title{left:59px;width:462px;top:888px;text-align:center;font-size:46px;color:var(--blue)}
.about-title span,.mission-title span,.team-title span{color:var(--green)}
.about-text{left:59px;top:974px;width:480px;font-size:13.4px;line-height:26.6px;color:var(--muted);text-align:justify;font-weight:300}
.about-text p+p{margin-top:26px}
.about-lead{left:58px;top:1322px;width:440px;font-size:17px;line-height:23px;color:var(--blue);font-weight:500}
.checks{left:64px;top:1386px;width:480px;list-style:none;font-size:12.5px;line-height:18px;color:var(--muted)}
.checks li{position:relative;padding-left:24px;margin-bottom:12px}
.checks li::before{content:"";position:absolute;left:0;top:2px;width:13px;height:13px;border:1.5px solid var(--green)}
.checks li::after{content:"";position:absolute;left:3px;top:4px;width:7px;height:4px;border-left:2px solid var(--green);border-bottom:2px solid var(--green);transform:rotate(-45deg)}

/* mission */
.mission-title{left:633px;width:480px;top:1480px;text-align:center;font-size:52px;color:var(--blue)}
.mission-body{left:634px;top:1572px;width:452px;font-size:13.4px;line-height:19.3px;color:var(--muted);text-align:justify}
.mission-body h4{color:var(--blue);font-size:13.5px;font-weight:600;margin:44px 0 12px}
.mission-body .note{margin-top:50px;font-style:italic;font-weight:700;color:#555;font-size:12.5px;line-height:16px;text-align:left}

/* banners */
.banner-title{left:200px;width:750px;text-align:center;color:#fff;font-size:46px;font-family:"Cabin",sans-serif}

/* investment */
.keypoint{font-size:19.5px;line-height:24px;color:#333}

/* advantages */
.adv{font-size:14.5px;line-height:19px;color:#444}

/* team */
.team-title{left:400px;width:400px;top:3858px;text-align:center;font-size:50px;color:var(--blue)}
.member{width:250px;text-align:center;font-size:11.5px;line-height:15px;color:#fff}
.member b{display:block;font-size:14px;letter-spacing:.3px}
.member em{display:block;font-style:normal;font-weight:600;font-size:12.5px;margin-bottom:14px}
.member p{margin-bottom:10px}
.on-blue b,.on-blue em{color:var(--green)}
.on-green b,.on-green em{color:var(--blue)}
.on-blue.alt b{color:#fff}
.arrow-btn{width:36px;height:36px;background:#222;color:#fff;display:flex;align-items:center;justify-content:center;font-size:20px}

/* footer */
.foot-brand{left:118px;top:4723px;font-family:"Cabin",sans-serif;font-weight:600;font-size:56px;color:var(--green);line-height:1}
.foot-brand small{display:block;font-size:32px;color:#fff;text-align:center;margin-top:2px}
.foot-col h5{color:#fff;font-family:"Cabin",sans-serif;font-size:18px;font-weight:600;letter-spacing:.5px;margin-bottom:14px}
.foot-col ul{list-style:none;color:#fff;font-size:14px;line-height:19.5px}
.foot-col ul li::before{content:"‹ ";}
.foot-contact{color:#fff;font-size:11.5px;line-height:21px}
.foot-contact span{display:inline-block;width:8px;height:8px;border-radius:50%;background:var(--green);margin-right:10px}
.foot-soc{display:flex;gap:22px;margin-top:4px}
.foot-soc i{width:10px;height:10px;background:#fff;border-radius:2px}
.call{color:#fff;font-family:"Cabin",sans-serif;font-weight:600;font-size:20px;line-height:24px}
.copyright{left:0;top:4853px;width:1200px;height:29px;background:var(--cyan);color:#e6f5fc;font-size:13px;display:flex;align-items:center;justify-content:center}
</style>
</head>
<body>

<svg class="shapes" viewBox="0 0 1200 4882" aria-hidden="false">
  <defs>
    <linearGradient id="spineGrad" x1="0" y1="0" x2="1" y2="1">
      <stop offset="0" stop-color="#1a9bd8"/><stop offset=".5" stop-color="#4fc3ef"/><stop offset="1" stop-color="#bfe9fa"/>
    </linearGradient>
    <linearGradient id="clinicGrad" x1="0" y1="0" x2="1" y2="1">
      <stop offset="0" stop-color="#c9d3da"/><stop offset=".5" stop-color="#a37a5e"/><stop offset="1" stop-color="#e9eef2"/>
    </linearGradient>
    <linearGradient id="modelGrad" x1="0" y1="0" x2="1" y2="1">
      <stop offset="0" stop-color="#f4f4f2"/><stop offset=".5" stop-color="#e7dcc4"/><stop offset="1" stop-color="#f6f6f4"/>
    </linearGradient>
  </defs>

  <!-- hero -->
  <polygon points="0,171 1200,171 1200,620 0,880" fill="var(--blue)"/>
  <polygon points="0,171 1200,171 1200,605 0,852" fill="#fff"/>
  <polygon points="490,190 1200,190 1200,605 490,742" fill="url(#spineGrad)" role="img" aria-label="Close-up of a model spinal column in blue light"/>
  <polygon points="0,190 490,190 490,742 0,838" fill="var(--green)"/>

  <!-- girl at clinic -->
  <polygon points="628,790 1140,690 1140,1300 628,1456" fill="var(--blue)"/>
  <polygon points="580,770 1112,668 1112,1280 580,1426" fill="url(#clinicGrad)" role="img" aria-label="Doctor examining a young girl's back"/>

  <!-- mission photo -->
  <polygon points="0,1600 575,1520 575,1560 0,1640" fill="#f2f3f4"/>
  <polygon points="58,1622 560,1545 560,2170 58,2224" fill="var(--green)"/>
  <polygon points="85,1592 578,1510 578,2140 85,2196" fill="url(#modelGrad)" role="img" aria-label="Hand pointing at a vertebrae model"/>

  <!-- keypoints banner -->
  <polygon points="284,2304 986,2304 1052,2393 360,2393" fill="var(--green)"/>
  <polygon points="199,2270 891,2270 948,2364 256,2364" fill="var(--blue)"/>

  <!-- investment panel -->
  <rect x="91" y="2480" width="1014" height="560" fill="var(--panel)" role="img" aria-label="Faded background of an operating room"/>
  <path d="M432 2512 A224 224 0 1 0 432 2960" fill="none" stroke="var(--blue)" stroke-width="3"/>
  <path d="M432 2512 A224 224 0 0 1 432 2960" fill="none" stroke="var(--blue)" stroke-width="3" stroke-dasharray="0"/>
  <circle cx="432" cy="2736" r="150" fill="var(--green)"/>
  <g fill="#fff">
    <circle cx="436" cy="2695" r="38"/><circle cx="436" cy="2695" r="22" fill="var(--green)"/>
    <text x="436" y="2707" font-family="Montserrat" font-weight="700" font-size="32" text-anchor="middle" fill="#fff">$</text>
    <path d="M340 2770 h60 l40 8 q40-10 80-32 q14 4 6 18 q-40 40-110 50 h-76z"/>
  </g>
  <g stroke="#fff" stroke-width="5" fill="var(--green)">
    <circle cx="565" cy="2573" r="38"/><circle cx="641" cy="2673" r="38"/>
    <circle cx="639" cy="2798" r="38"/><circle cx="565" cy="2914" r="38"/>
  </g>
  <g fill="none" stroke="var(--blue)" stroke-width="3">
    <circle cx="565" cy="2573" r="42"/><circle cx="641" cy="2673" r="42"/>
    <circle cx="639" cy="2798" r="42"/><circle cx="565" cy="2914" r="42"/>
  </g>
  <g fill="#fff">
    <rect x="547" y="2567" width="36" height="16" rx="3"/><circle cx="565" cy="2562" r="6"/>
    <circle cx="641" cy="2673" r="13" fill="none" stroke="#fff" stroke-width="4"/>
    <circle cx="639" cy="2790" r="8"/><rect x="625" y="2800" width="28" height="14" rx="4"/>
    <circle cx="565" cy="2920" r="14"/><text x="565" y="2926" font-size="16" font-weight="700" text-anchor="middle" fill="var(--green)" font-family="Montserrat">$</text>
  </g>

  <!-- advantages banner -->
  <polygon points="284,3125 986,3125 1052,3214 360,3214" fill="var(--green)"/>
  <polygon points="199,3091 891,3091 948,3185 256,3185" fill="var(--blue)"/>
  <rect x="280" y="3270" width="820" height="560" fill="#f8f8f9" role="img" aria-label="Faded background of medical imaging"/>

  <!-- advantage icons -->
  <g>
    <g fill="var(--blue)" stroke="#fff" stroke-width="4">
      <circle cx="157" cy="3413" r="48"/><circle cx="491" cy="3413" r="48"/><circle cx="827" cy="3413" r="48"/>
      <circle cx="157" cy="3555" r="48"/><circle cx="491" cy="3555" r="48"/><circle cx="827" cy="3555" r="48"/>
      <circle cx="157" cy="3701" r="48"/><circle cx="491" cy="3701" r="48"/><circle cx="827" cy="3701" r="48"/>
    </g>
    <g fill="none" stroke="var(--blue)" stroke-width="2">
      <circle cx="157" cy="3413" r="52"/><circle cx="491" cy="3413" r="52"/><circle cx="827" cy="3413" r="52"/>
      <circle cx="157" cy="3555" r="52"/><circle cx="491" cy="3555" r="52"/><circle cx="827" cy="3555" r="52"/>
      <circle cx="157" cy="3701" r="52"/><circle cx="491" cy="3701" r="52"/><circle cx="827" cy="3701" r="52"/>
    </g>
    <g fill="#fff">
      <rect x="137" y="3418" width="8" height="14"/><rect x="149" y="3408" width="8" height="24"/><rect x="161" y="3396" width="8" height="36"/>
      <path d="M165 3388 l10 10 h-20z"/>
      <path d="M476 3398 h8 v-8 M506 3398 h-8 v-8 M476 3428 h8 v8 M506 3428 h-8 v8" stroke="#fff" stroke-width="3" fill="none"/>
      <circle cx="491" cy="3402" r="5"/><path d="M486 3410 h10 l4 16 h-5 l-4-8 -4 8 h-5z"/>
      <rect x="815" y="3392" width="24" height="24" rx="3"/><path d="M811 3420 h32 q-6 14-20 14 h-12z"/>
      <circle cx="157" cy="3545" r="14"/><path d="M135 3580 q22-26 44 0z"/>
      <path d="M491 3530 l14 16 h-9 v28 h-10 v-28 h-9z"/>
      <circle cx="827" cy="3560" r="16"/><circle cx="813" cy="3544" r="6"/><circle cx="841" cy="3544" r="6"/>
      <path d="M145 3690 a14 14 0 1 0 24 0" stroke="#fff" stroke-width="4" fill="none"/><rect x="154" y="3680" width="6" height="16"/>
      <rect x="472" y="3712" width="38" height="8"/><rect x="472" y="3700" width="10" height="12"/><circle cx="491" cy="3688" r="7"/>
      <path d="M810 3700 h10 v22 h-10z M823 3700 l8-16 q6 0 5 8 l-2 6 h10 q5 2 3 8 l-4 16 h-20z"/>
    </g>
  </g>

  <!-- team panels -->
  <polygon points="53,4130 303,4060 303,4500 53,4530" fill="var(--blue)"/>
  <polygon points="295,4055 552,3985 552,4450 295,4505" fill="var(--green)"/>
  <polygon points="543,3995 800,3925 800,4395 543,4455" fill="var(--blue)"/>
  <polygon points="790,3975 1105,3905 1105,4300 790,4400" fill="var(--green)"/>
  <g stroke="#fff" stroke-width="4" fill="#c9ced3">
    <circle cx="180" cy="4209" r="76" role="img" aria-label="Portrait of the founder and CEO"/>
    <circle cx="417" cy="4181" r="76" role="img" aria-label="Portrait of the chief science officer"/>
    <circle cx="645" cy="4130" r="76" role="img" aria-label="Portrait of the VP of R&amp;D and operations"/>
    <circle cx="920" cy="4114" r="76" role="img" aria-label="Portrait of the senior R&amp;D engineer"/>
  </g>

  <!-- footer -->
  <polygon points="0,4500 1200,4430 1200,4560 0,4640" fill="#eef0f1"/>
  <polygon points="0,4640 810,4500 810,4540 1200,4480 1200,4853 0,4853" fill="var(--blue)"/>
  <polygon points="0,4640 810,4500 810,4508 0,4648" fill="var(--green)"/>
</svg>

<!-- header -->
<div class="abs brand">Vertara<small>Surgical</small></div>
<div class="abs phone-tab">&#9742; (555) 310 4827</div>
<div class="abs follow">Follow Us</div>
<div class="abs social"><span></span><span></span><span></span><span></span><span></span><span></span></div>
<nav class="abs nav">
  <a class="home" href="#">Home</a>
  <a href="#" style="left:243px">About</a>
  <a href="#" style="left:355px">Team</a>
  <a href="#" style="left:472px">Benefits</a>
  <a href="#" style="left:602px">Investment</a>
  <a href="#" style="left:777px">Contact Us</a>
</nav>
<div class="abs vbt-btn">VBT TETHERING</div>

<!-- hero -->
<h1 class="abs hero-title">Solving<br>Children’s<br>Scoliosis</h1>
<div class="abs hero-side">
  <h2>VERTEBRAL BODY TETHERING</h2>
  <p>Non-fusion scoliosis correction<br>allowing for non-surgical dynamic<br>adjustment of implants over time.</p>
</div>
<div class="abs know-more">KNOW MORE</div>

<!-- about -->
<h2 class="abs about-title">About <span>us</span></h2>
<div class="abs about-text">
  <p>Scoliosis affects an estimated 15 million children in the US. Vertara Surgical, Inc. was formed to develop novel orthopedic implants focusing on non-fusion scoliosis correction and limb lengthening. The products incorporate a dynamic magnetic technology permitting non-surgical adjustment of the implants over time.</p>
  <p>Vertara has filed IP and begun development on a dynamic spinal tethering system for non-fusion growth modulation in pediatric scoliosis patients. This system employs a magnetically driven nonsurgical adjustment mechanism activated by an external controller. Vertara has also sub-licensed IP controlled by Westbay University relating to a magnetically-driven growing rod technology.</p>
</div>
<div class="abs about-lead">This technology development has led to two future product lines:</div>
<ul class="abs checks">
  <li>A magnetically growing in tramedullary rod for limb lengthening in trauma and pediatric deformity</li>
  <li>A magnetically growing rod for early onset scoliosis patients</li>
</ul>

<!-- mission -->
<h2 class="abs mission-title">Our <span>Mission</span></h2>
<div class="abs mission-body">
  <p>Develop novel technologies focusing on non-fusion scoliosis correction allowing for non-surgical dynamic adjustment of implants over time.</p>
  <h4>THE PROBLEM</h4>
  <p>Current pediatric scoliosis treatment options, have significant limitations. Bracing can slow progression, but does not correct the spine and is a long term treatment that poses psychological, social and emotional challenges at a critical stage in life. Fusion is irreversible, NO motion capability causes significant change in life activities, can create adjacent segment disease due to stress concentration and increased segmental motion leads to secondary operations in adulthood</p>
  <h4>OUR SOLUTION</h4>
  <p>Vertebral body tethering allows continued skeletal growth of spine, preserves partial motion, is a single treatment event, does not impact activity and has little impact on appearance.</p>
  <p class="note">Tethering has non-invasive adjustability where the system can be tensioned or loosened over time to manage growth. This actuation is achieved by an external controller.</p>
</div>

<!-- investment -->
<h2 class="abs banner-title" style="top:2288px">Keypoints for Investment</h2>
<div class="abs keypoint" style="left:618px;top:2530px">Vertebral Body Tethering procedure<br>potential non-fusion game-changer</div>
<div class="abs keypoint" style="left:699px;top:2660px">Dynamic system is the key</div>
<div class="abs keypoint" style="left:694px;top:2772px">Experienced team with a previous<br>successful exit in the spinal implant market</div>
<div class="abs keypoint" style="left:621px;top:2890px">$20-30M total capital<br>$200-$600M Exit within 5 years</div>

<!-- advantages -->
<h2 class="abs banner-title" style="top:3109px">Advantages of VBT over Fusion</h2>
<div class="abs adv" style="left:220px;top:3395px">Continued<br>skeletal growth</div>
<div class="abs adv" style="left:554px;top:3395px">Partial Motion<br>Preservation</div>
<div class="abs adv" style="left:891px;top:3395px">Single treatment<br>event</div>
<div class="abs adv" style="left:220px;top:3537px">Little impact on<br>activity &amp; appearance</div>
<div class="abs adv" style="left:554px;top:3537px">Does not<br>“burn any bridge”</div>
<div class="abs adv" style="left:891px;top:3537px">66% Cost Savings<br>($50K compared to $150K)</div>
<div class="abs adv" style="left:220px;top:3674px">50% Saving in Surgery<br>Time (1.5-2 hrs<br>compared to 4-6 hrs)</div>
<div class="abs adv" style="left:554px;top:3674px">50% Saving in Hospital<br>Stay (2-3 days<br>compared to 6-7 days)</div>
<div class="abs adv" style="left:891px;top:3664px">Confirmed improved<br>self-confidence for<br>surgical recipients</div>

<!-- team -->
<h2 class="abs team-title">Our <span>Team</span></h2>
<div class="abs member on-blue" style="left:55px;top:4300px">
  <b>GRAHAM ELLISON</b><em>Founder &amp; CEO</em>
  <p>Co-founder &amp; CEO<br>of Arcline Innovations-<br>Acquired by Halden Medical in 2014</p>
  <p>Leadership positions at<br>Northway Labs and Calder Health</p>
</div>
<div class="abs member on-green" style="left:297px;top:4272px">
  <b>RAVI MENON PH.D.</b><em style="color:#fff">Co-Founder Chief Science Officer</em>
  <p>Previous Chief Science<br>Officer at Arcline Innovations</p>
  <p>Previous leadership<br>positions at Axilon,<br>Halden Medical and Brantley Ortho</p>
</div>
<div class="abs member on-blue alt" style="left:547px;top:4220px">
  <b>PETER LOWRY</b><em>Co-Founder VP R&amp;D<br>and Operations</em>
  <p>Previous VP of R&amp;D at<br>Arcline Innovations</p>
  <p>Previous leadership<br>positions at Spineform,<br>Corvale, Ostrava Med &amp;<br>Redfield Technologies</p>
</div>
<div class="abs member on-green" style="left:800px;top:4200px">
  <b>EVAN MARSH</b><em style="color:#fff">Co-founder and<br>Senior R&amp;D Engineer</em>
  <p>Senior R&amp;D engineer at<br>Westbay University,<br>North Campus</p>
</div>
<div class="abs arrow-btn" style="left:53px;top:4213px">‹</div>
<div class="abs arrow-btn" style="left:1104px;top:4128px">›</div>

<!-- footer -->
<div class="abs foot-brand">Vertara<small>Surgical</small></div>
<div class="abs foot-col" style="left:417px;top:4608px">
  <h5>QUICK LINKS</h5>
  <ul><li>Home</li><li>About</li><li>Team</li><li>VBT Tethering</li><li>Benefits</li><li>Investment</li><li>Contact</li></ul>
</div>
<div class="abs foot-col" style="left:677px;top:4602px">
  <h5>CONTACT</h5>
  <div class="foot-contact" style="margin-top:50px">
    <div><span></span>(555) 310 4827</div>
    <div><span></span>(555) 310 4890</div>
    <div><span></span>info@vertarasurgical.com</div>
    <div><span></span>www.vertarasurgical.com</div>
  </div>
</div>
<div class="abs foot-col" style="left:923px;top:4592px">
  <h5>FOLLOW US ON</h5>
  <div class="foot-soc"><i></i><i></i><i></i><i></i></div>
  <div style="width:20px;height:2px;background:#fff;margin:42px 0 20px"></div>
  <div class="call">CALL US ON<br>(555) 310 4827</div>
</div>
<div class="abs copyright">© 2020 Vertara Surgical &nbsp;|&nbsp; Privacy Policy &nbsp;|&nbsp; User Agreement</div>

</body>
</html>
```